Design an investor pitch deck for Brindlecart.io

We delivered a killer investor pitch to a group of investors last week and have been asked for a deck. we need to follow up with a killer printed version. I have produced the attached file using free images from vistaloom. Feel free to change the imagery as you see fit. Check out brindlecart.io to get a feel for the look and feel we have right now.

Target Market(s)

Investors

Industry/Entity Type

Software

Font styles to use
Sans Serif
Other font styles liked:
• Helvetica

Requirements
Must have
• A new version of each of the pages in the example documents. Needs to be slick and professional
Nice to have
• Other layouts in case I add further slides
Should not have
• Childish or dated shapes or designs

```html
<!DOCTYPE html>
<html lang="en">
<head>
<meta charset="utf-8">
<title>Brindlecart.io — Investor Deck</title>
<link rel="stylesheet" href="https://fonts.googleapis.com/css2?family=Montserrat:wght@400;500;600;700&display=swap">
<style>
:root{
  --grey:#b9b9b9;
  --ink:#2c2c2c;
  --icon:#6f6f6f;
  --blue:#2d4f9c;
  --navy:#0f1f45;
  --gold:#c9a04a;
  --orange:#f6a623;
  --circle:#cfcfcf;
  --paper:#ffffff;
}
*{box-sizing:border-box;margin:0;padding:0}
html,body{width:970px;height:1200px;overflow:hidden;background:var(--paper)}
body{position:relative;font-family:"Montserrat",Helvetica,Arial,sans-serif;color:var(--ink)}
.slide{position:absolute;width:444px;height:122px;overflow:hidden;background:var(--paper)}
.hdr{position:absolute;left:0;top:0;width:100%;height:17px;background:var(--grey);color:#fff;font-size:10px;letter-spacing:1.5px;text-align:center;line-height:17px}
.hdr .dot{position:absolute;left:10px;top:3px;width:11px;height:11px;border-radius:50%;background:#fff}
.abs{position:absolute}
.tiny{font-size:5.2px;line-height:1.25}
.small{font-size:6.5px;line-height:1.25}
.brand{font-weight:700;letter-spacing:1px}
.photo-city{background:linear-gradient(135deg,#0c1a3a 0%,#1f3a7a 45%,#3b5fa8 70%,#142650 100%)}
.photo-wrist{background:linear-gradient(135deg,#c9b8a8,#8c6e5a 55%,#d8d0c8)}
.photo-street{background:linear-gradient(135deg,#2b2b2b,#6a6560 50%,#e6dfd2)}
.photo-globe{background:radial-gradient(circle at 40% 45%,#e8d8b8,#b88a5a 55%,#6b4a2e)}
.photo-map{background:linear-gradient(160deg,#e9ecef,#cfd8e0 50%,#f4f4f4)}
.ring,.gold-ring,.tile{position:absolute;display:flex;align-items:center;justify-content:center}
.ring{border:1px solid var(--grey);border-radius:50%;background:#fff;color:var(--icon)}
.gold-ring{border:1.5px solid var(--gold);border-radius:50%;background:#fff;color:var(--gold)}
.tile{border:1px solid #ddd;background:#fff;color:var(--gold)}
.tile.orange{border:none;border-radius:4px;background:var(--orange);color:#fff}
.bare{position:absolute;color:var(--gold)}
.ico{width:10px;height:10px}
.ico.md{width:13px;height:13px}
.ico.lg{width:16px;height:16px}
.partner{position:absolute;font-size:6.5px;font-weight:700}
.bar-row{position:absolute;height:9px;background:var(--grey);color:#fff;font-size:6.5px;line-height:9px;padding-left:8px;letter-spacing:.5px}
.gold{color:var(--gold)}
.center{text-align:center}
.contact{position:absolute;font-size:5.2px;line-height:1.25;text-align:right;color:#fff}
</style>
</head>
<body>

<svg width="0" height="0" style="position:absolute" aria-hidden="true">
  <defs>
    <symbol id="i-network" viewBox="0 0 24 24"><g fill="none" stroke="currentColor" stroke-width="1.6"><circle cx="5" cy="6" r="2.2"/><circle cx="19" cy="6" r="2.2"/><circle cx="12" cy="18" r="2.2"/><path d="M7 7l4 9M17 7l-4 9M7.2 6h9.6"/></g></symbol>
    <symbol id="i-globe" viewBox="0 0 24 24"><g fill="none" stroke="currentColor" stroke-width="1.6"><circle cx="12" cy="12" r="9"/><ellipse cx="12" cy="12" rx="4" ry="9"/><path d="M3 12h18"/></g></symbol>
    <symbol id="i-link" viewBox="0 0 24 24"><g fill="none" stroke="currentColor" stroke-width="1.6"><rect x="2" y="8" width="11" height="8" rx="4"/><rect x="11" y="8" width="11" height="8" rx="4"/></g></symbol>
    <symbol id="i-people" viewBox="0 0 24 24"><g fill="none" stroke="currentColor" stroke-width="1.6"><circle cx="8" cy="8" r="3"/><circle cx="16" cy="8" r="3"/><path d="M2 20c0-4 3-6 6-6s6 2 6 6M12 15c1-1 2.5-1 4-1 3 0 6 2 6 6"/></g></symbol>
    <symbol id="i-clock" viewBox="0 0 24 24"><g fill="none" stroke="currentColor" stroke-width="1.6"><circle cx="12" cy="12" r="9"/><path d="M12 7v5l3 3"/></g></symbol>
    <symbol id="i-cloud" viewBox="0 0 24 24"><path d="M7 18h11a4 4 0 000-8 6 6 0 00-11-1 4.5 4.5 0 000 9z" fill="none" stroke="currentColor" stroke-width="1.6"/></symbol>
    <symbol id="i-monitor" viewBox="0 0 24 24"><g fill="none" stroke="currentColor" stroke-width="1.6"><rect x="3" y="4" width="18" height="12" rx="1"/><path d="M9 20h6M12 16v4"/></g></symbol>
    <symbol id="i-phone" viewBox="0 0 24 24"><g fill="none" stroke="currentColor" stroke-width="1.6"><rect x="7" y="2" width="10" height="20" rx="2"/><path d="M11 18h2"/></g></symbol>
    <symbol id="i-pin" viewBox="0 0 24 24"><g fill="none" stroke="currentColor" stroke-width="1.6"><path d="M12 22s7-7 7-12a7 7 0 00-14 0c0 5 7 12 7 12z"/><circle cx="12" cy="10" r="2.5"/></g></symbol>
    <symbol id="i-tag" viewBox="0 0 24 24"><g fill="none" stroke="currentColor" stroke-width="1.6"><path d="M3 12V4h8l10 10-8 8z"/><circle cx="7.5" cy="8.5" r="1.5"/></g></symbol>
    <symbol id="i-coin" viewBox="0 0 24 24"><g fill="none" stroke="currentColor" stroke-width="1.6"><circle cx="12" cy="12" r="9"/><path d="M15 9c-.8-1.2-5-1.6-5 .8 0 2.6 5 1.6 5 4.4 0 2-4 2.2-5.4.6M12 6v12"/></g></symbol>
    <symbol id="i-card" viewBox="0 0 24 24"><g fill="none" stroke="currentColor" stroke-width="1.6"><rect x="2" y="5" width="20" height="14" rx="2"/><path d="M2 10h20M6 15h4"/></g></symbol>
    <symbol id="i-star" viewBox="0 0 24 24"><path d="M12 3l2.7 5.6 6.1.9-4.4 4.3 1 6.1L12 17l-5.4 2.9 1-6.1L3.2 9.5l6.1-.9z" fill="none" stroke="currentColor" stroke-width="1.6"/></symbol>
    <symbol id="i-target" viewBox="0 0 24 24"><g fill="none" stroke="currentColor" stroke-width="1.6"><circle cx="12" cy="12" r="9"/><circle cx="12" cy="12" r="5"/><circle cx="12" cy="12" r="1.5"/></g></symbol>
    <symbol id="i-eye" viewBox="0 0 24 24"><g fill="none" stroke="currentColor" stroke-width="1.6"><path d="M2 12s4-7 10-7 10 7 10 7-4 7-10 7S2 12 2 12z"/><circle cx="12" cy="12" r="3"/></g></symbol>
    <symbol id="i-route" viewBox="0 0 24 24"><g fill="none" stroke="currentColor" stroke-width="1.6"><circle cx="5" cy="18" r="2.5"/><circle cx="19" cy="6" r="2.5"/><path d="M7.5 18H15a3 3 0 000-6H9a3 3 0 010-6h7.5"/></g></symbol>
  </defs>
</svg>

<!-- Title A -->
<section class="slide" style="left:0;top:0;width:448px;height:124px">
  <div class="abs photo-wrist" role="img" aria-label="Photo of a person checking a wristwatch" style="left:0;top:0;width:228px;height:124px"></div>
  <div class="abs" style="left:313px;top:20px;width:12px;height:12px;border-radius:50%;background:var(--navy)"></div>
  <div class="abs brand" style="left:259px;top:40px;font-size:18px;color:var(--navy)">Brindlecart</div>
  <div class="abs small" style="left:259px;top:62px;font-size:8.5px;width:160px">Waiting sucks. Brindlecart makes it better.</div>
  <div class="contact" style="right:8px;top:104px;color:var(--ink)">Corin Ashdale<br>Founder @ Harbourline Engineering<br>corin@brindlecart.io</div>
</section>

<!-- Title B -->
<section class="slide" style="left:472px;top:4px;width:446px;height:124px">
  <div class="abs photo-city" role="img" aria-label="Night city skyline overlaid with a glowing network of delivery icons" style="left:3px;top:26px;width:440px;height:78px"></div>
  <div class="abs" style="left:0;top:0;width:264px;height:44px;background:var(--grey)"></div>
  <div class="abs" style="left:10px;top:8px;width:14px;height:14px;border-radius:50%;background:#fff"></div>
  <div class="abs brand" style="left:56px;top:7px;font-size:16px;color:#fff">Brindlecart</div>
  <div class="abs small" style="left:56px;top:28px;color:#fff;font-size:7.5px">Waiting sucks. Brindlecart makes it better.</div>
  <div class="abs" style="right:0;top:98px;width:134px;height:26px;background:var(--grey)"></div>
  <div class="contact" style="right:5px;top:102px">Corin Ashdale<br>Founder @ Harbourline Engineering<br>corin@brindlecart.io</div>
</section>

<!-- Title C -->
<section class="slide" style="left:6px;top:132px;width:446px;height:124px">
  <div class="abs photo-city" role="img" aria-label="Night city skyline overlaid with a glowing network of delivery icons" style="left:0;top:44px;width:446px;height:80px"></div>
  <div class="abs" style="left:0;top:0;width:446px;height:44px;background:var(--grey)"></div>
  <div class="abs" style="left:22px;top:8px;width:14px;height:14px;border-radius:50%;background:#fff"></div>
  <div class="abs brand" style="left:52px;top:8px;font-size:16px;color:#fff">Brindlecart</div>
  <div class="abs small" style="left:52px;top:29px;color:#fff;font-size:7.5px">Waiting sucks. Brindlecart makes it better.</div>
  <div class="abs" style="right:0;top:98px;width:126px;height:26px;background:var(--blue)"></div>
  <div class="contact" style="right:5px;top:102px">Corin Ashdale<br>Founder @ Harbourline Engineering<br>corin@brindlecart.io</div>
</section>

<!-- Title D -->
<section class="slide" style="left:482px;top:138px;width:446px;height:124px">
  <div class="abs photo-city" role="img" aria-label="Night city skyline overlaid with a glowing network of delivery icons" style="left:0;top:0;width:446px;height:64px"></div>
  <div class="abs" style="left:0;top:64px;width:136px;height:60px;background:var(--grey)"></div>
  <div class="abs" style="left:50px;top:74px;width:16px;height:16px;border-radius:50%;background:#fff"></div>
  <div class="abs tiny" style="left:10px;top:100px;color:#fff">Corin Ashdale<br>Founder @ Harbourline Engineering<br>corin@brindlecart.io</div>
  <div class="abs" style="left:136px;top:64px;width:310px;height:60px;background:var(--blue)"></div>
  <div class="abs brand" style="left:156px;top:76px;font-size:16px;color:#fff">Brindlecart</div>
  <div class="abs small" style="left:156px;top:96px;color:#fff;font-size:8px">Waiting Sucks. Brindlecart Makes It Better.</div>
</section>

<!-- Big Idea A -->
<section class="slide" style="left:18px;top:268px;width:442px;height:124px">
  <div class="hdr"><span class="dot"></span>The Big Idea in 125 words</div>
  <div class="abs center" style="left:0;top:24px;width:442px;font-size:8.5px;line-height:1.3">Waiting sucks. Live tracking makes waiting for deliveries<br>and services less painful. Brindlecart makes it easy.</div>
  <div class="ring" style="left:54px;top:49px;width:36px;height:14px"><svg class="ico"><use href="#i-network"/></svg></div>
  <div class="ring" style="left:182px;top:49px;width:36px;height:14px"><svg class="ico"><use href="#i-link"/></svg></div>
  <div class="ring" style="left:336px;top:48px;width:36px;height:14px"><svg class="ico"><use href="#i-people"/></svg></div>
  <div class="abs tiny" style="left:16px;top:68px;width:122px">You could track your pizza in realtime since 2015. Now business that still make people wait without a live tracking link are giving an unnecessarily poor customer experience and their brand suffers greatly.</div>
  <div class="abs tiny" style="left:150px;top:66px;width:124px">Why doesn't everyone send tracking links now? Why can't we track important things like emergency services or mission critical business deliveries? Legacy processes, complex last-mile arrangements through multiple providers, lack of a cheap and easy solution.</div>
  <div class="abs tiny" style="left:296px;top:66px;width:126px">Brindlecart is the cleanest, simplest way to give customers a tracking link, while giving managers, drivers and developers the best possible tools to provide a great last-mile service cheaply and easily while promoting their brand and getting customer feedback.</div>
</section>

<!-- Big Idea B -->
<section class="slide" style="left:480px;top:270px;width:448px;height:126px">
  <div class="abs photo-street" role="img" aria-label="Sunlit city street with trees and buildings" style="left:0;top:0;width:207px;height:126px"></div>
  <div class="abs center" style="left:4px;top:24px;width:200px;color:#fff;font-size:14.5px;font-weight:600;line-height:1.25">The Big Idea<br>in 125 words</div>
  <div class="abs center" style="left:8px;top:62px;width:192px;color:#fff;font-size:8px;line-height:1.4">Waiting sucks. Live tracking makes waiting for deliveries and services less painful. Brindlecart makes it easy.</div>
  <div class="ring" style="left:218px;top:8px;width:18px;height:18px"><svg class="ico"><use href="#i-network"/></svg></div>
  <div class="ring" style="left:218px;top:44px;width:18px;height:18px"><svg class="ico"><use href="#i-link"/></svg></div>
  <div class="ring" style="left:218px;top:82px;width:18px;height:18px"><svg class="ico"><use href="#i-people"/></svg></div>
  <div class="abs tiny" style="left:244px;top:10px;width:196px">You could track your pizza in realtime since 2015. Now business that still make people wait without a live tracking link are giving an unnecessarily poor customer experience and their brand suffers greatly.</div>
  <div class="abs tiny" style="left:244px;top:44px;width:196px">Why doesn't everyone send tracking links now? Why can't we track important things like emergency services or mission critical business deliveries? Legacy processes, complex last-mile arrangements through multiple providers, lack of a cheap and easy solution.</div>
  <div class="abs tiny" style="left:244px;top:82px;width:196px">Brindlecart is the cleanest, simplest way to give customers a tracking link, while giving managers, drivers and developers the best possible tools to provide a great last-mile service cheaply and easily while promoting their brand and reinforcing their brand and getting customer feedback.</div>
  <div class="abs" style="left:430px;top:114px;width:8px;height:8px;border-radius:50%;background:var(--blue)"></div>
</section>

<!-- Why Now A -->
<section class="slide" style="left:24px;top:400px;width:442px;height:122px">
  <div class="hdr"><span class="dot"></span>Why Now?</div>
  <div class="ring" style="left:54px;top:34px;width:110px;height:46px"></div>
  <div class="ring" style="left:168px;top:34px;width:110px;height:46px"></div>
  <div class="ring" style="left:284px;top:32px;width:110px;height:46px"></div>
  <svg class="abs" style="left:160px;top:48px" width="12" height="18" viewBox="0 0 12 18"><polygon points="2,1 11,9 2,17" fill="var(--grey)"/></svg>
  <svg class="abs" style="left:275px;top:48px" width="12" height="18" viewBox="0 0 12 18"><polygon points="2,1 11,9 2,17" fill="var(--grey)"/></svg>
  <div class="abs small center" style="left:54px;top:44px;width:110px">Simple<br>Global<br>Deployment</div>
  <div class="abs small center" style="left:168px;top:44px;width:110px">Success of<br>best in class<br>integration</div>
  <div class="abs small center" style="left:284px;top:42px;width:110px">Shifting<br>Customer<br>Expectation</div>
  <div class="partner" style="left:88px;top:88px;color:#e08a1a">cloudhaven</div>
  <div class="partner" style="left:96px;top:102px;color:#c0392b">pingwire</div>
  <div class="partner" style="left:210px;top:84px;color:#5b5fd6">paylane</div>
  <div class="partner" style="left:196px;top:98px;color:#1aa0d8">ledgio</div>
  <div class="partner" style="left:230px;top:98px">chatterbox</div>
  <div class="partner" style="left:314px;top:82px">shopnow</div>
  <div class="partner" style="left:362px;top:84px;color:#1d5aa8">Pizzaroo</div>
  <div class="partner" style="left:312px;top:98px;color:#00a89c">dashbite</div>
  <div class="partner" style="left:356px;top:100px">Ridello</div>
</section>

<!-- Why Now B -->
<section class="slide" style="left:490px;top:404px;width:442px;height:122px">
  <div class="hdr"><span class="dot"></span>Why Now?</div>
  <div class="abs photo-map" role="img" aria-label="Screenshot of the dispatch dashboard with a city map and job list" style="left:0;top:21px;width:158px;height:100px;border:1px solid #ddd"></div>
  <div class="ring" style="left:166px;top:26px;width:22px;height:14px"><svg class="ico"><use href="#i-globe"/></svg></div>
  <div class="ring" style="left:166px;top:58px;width:22px;height:14px"><svg class="ico"><use href="#i-link"/></svg></div>
  <div class="ring" style="left:166px;top:92px;width:22px;height:14px"><svg class="ico"><use href="#i-people"/></svg></div>
  <div class="abs small" style="left:212px;top:26px">Simple Global<br>Deployment</div>
  <div class="abs small" style="left:212px;top:62px">Success of best-in-<br>class integration</div>
  <div class="abs small" style="left:212px;top:96px">Shifting Customer<br>Expectation</div>
  <div class="partner" style="left:336px;top:28px;color:#e08a1a">cloudhaven</div>
  <div class="partner" style="left:392px;top:28px;color:#c0392b">pingwire</div>
  <div class="partner" style="left:332px;top:64px;color:#1aa0d8">ledgio</div>
  <div class="partner" style="left:370px;top:58px">chatterbox</div>
  <div class="partner" style="left:376px;top:70px;color:#5b5fd6">paylane</div>
  <div class="partner" style="left:336px;top:92px">shopnow</div>
  <div class="partner" style="left:386px;top:94px;color:#1d5aa8">Pizzaroo</div>
  <div class="partner" style="left:338px;top:106px;color:#00a89c">dashbite</div>
  <div class="partner" style="left:388px;top:108px">Ridello</div>
</section>

<!-- Why Now C -->
<section class="slide" style="left:14px;top:530px;width:444px;height:122px">
  <div class="hdr"><span class="dot"></span>Why Now?</div>
  <div class="abs" style="left:150px;top:26px;width:142px;height:92px;border-radius:50%;background:var(--circle)"></div>
  <div class="abs" style="left:210px;top:60px;width:22px;height:22px;border-radius:50%;background:#fff"></div>
  <div class="gold-ring" style="left:208px;top:32px;width:24px;height:14px"><svg class="ico"><use href="#i-globe"/></svg></div>
  <div class="gold-ring" style="left:144px;top:66px;width:24px;height:14px"><svg class="ico"><use href="#i-link"/></svg></div>
  <div class="gold-ring" style="left:280px;top:68px;width:24px;height:14px"><svg class="ico"><use href="#i-people"/></svg></div>
  <div class="abs small center" style="left:146px;top:20px;width:150px">Simple Global Deployment</div>
  <div class="abs small center" style="left:30px;top:68px;width:110px">Success of best in<br>class integration</div>
  <div class="abs small" style="left:314px;top:68px">Shifting Customer<br>Expectation</div>
  <div class="partner" style="left:320px;top:26px;color:#e08a1a">cloudhaven</div>
  <div class="partner" style="left:380px;top:26px;color:#c0392b">pingwire</div>
  <div class="partner" style="left:40px;top:92px;color:#1aa0d8">ledgio</div>
  <div class="partner" style="left:70px;top:88px">chatterbox</div>
  <div class="partner" style="left:72px;top:100px;color:#5b5fd6">paylane</div>
  <div class="partner" style="left:314px;top:88px">shopnow</div>
  <div class="partner" style="left:354px;top:90px;color:#1d5aa8">Pizzaroo</div>
  <div class="partner" style="left:310px;top:104px;color:#00a89c">dashbite</div>
  <div class="partner" style="left:354px;top:104px">Ridello</div>
</section>

<!-- Solution -->
<section class="slide" style="left:486px;top:530px;width:442px;height:122px">
  <div class="hdr"><span class="dot"></span>The Solution</div>
  <div class="bare" style="left:58px;top:46px"><svg class="ico lg"><use href="#i-cloud"/></svg></div>
  <div class="abs tiny" style="left:34px;top:70px;width:80px">Integrations with common sources of jobs and automation tools like Linkflow</div>
  <svg class="abs" style="left:112px;top:50px" width="40" height="14" viewBox="0 0 40 14"><line x1="4" y1="7" x2="36" y2="7" stroke="#bbb"/></svg>
  <div class="bare" style="left:164px;top:47px"><svg class="ico lg"><use href="#i-monitor"/></svg></div>
  <div class="abs tiny" style="left:148px;top:70px;width:78px">Simple web portal for keeping track of staff and jobs in realtime</div>
  <svg class="abs" style="left:196px;top:30px" width="50" height="60" viewBox="0 0 50 60">
    <polyline points="0,26 24,26" fill="none" stroke="#bbb"/>
    <polyline points="24,8 24,46" fill="none" stroke="#bbb"/>
    <polyline points="24,8 40,8" fill="none" stroke="#bbb"/>
    <polyline points="24,46 40,46" fill="none" stroke="#bbb"/>
    <polygon points="40,5 45,8 40,11" fill="#bbb"/>
    <polygon points="40,43 45,46 40,49" fill="#bbb"/>
  </svg>
  <div class="bare" style="left:251px;top:31px"><svg class="ico md"><use href="#i-phone"/></svg></div>
  <div class="bare" style="left:251px;top:69px"><svg class="ico md"><use href="#i-pin"/></svg></div>
  <div class="abs tiny" style="left:326px;top:30px;width:110px">A clean, intuitive driver app with 1-click activation of the tracking link</div>
  <div class="abs tiny" style="left:326px;top:68px;width:110px">A customer tracking link sent via SMS and opened with 1 click</div>
</section>

<!-- Market Size -->
<section class="slide" style="left:0;top:662px;width:428px;height:116px">
  <div class="hdr"><span class="dot"></span>Market Size</div>
  <div class="abs tiny" style="left:2px;top:34px;width:180px;font-size:5.8px;line-height:1.3">
    1.&nbsp;&nbsp;1.35 billion annual deliveries from ecommerce by 2025 in UK<br><br>
    2.&nbsp;&nbsp;global e-commerce deliveries expected to exceed 24 billion*<br><br>
    3.&nbsp;&nbsp;Based on our bulk discount effective rate of USD12c per job total market will be USD2.8bn in 2018
  </div>
  <div class="abs tiny" style="left:2px;top:96px;width:180px;color:#999">*Source: annual parcel delivery study, 2018 edition</div>
  <div class="abs tiny" style="left:198px;top:22px;color:#1aa0d8">Parcel volumes by country (billions per year)</div>
  <svg class="abs" style="left:198px;top:30px" width="222" height="80" viewBox="0 0 222 80">
    <g fill="#1aa0d8">
      <rect x="6" y="4" width="12" height="62"/><rect x="26" y="8" width="12" height="58"/>
      <rect x="46" y="18" width="12" height="48"/><rect x="66" y="26" width="12" height="40"/>
      <rect x="86" y="34" width="12" height="32"/><rect x="106" y="40" width="12" height="26"/>
      <rect x="126" y="46" width="12" height="20"/><rect x="146" y="50" width="12" height="16"/>
      <rect x="166" y="54" width="12" height="12"/><rect x="186" y="56" width="12" height="10"/>
      <rect x="206" y="58" width="12" height="8"/>
    </g>
    <g fill="#1f2d4a">
      <rect x="6" y="4" width="12" height="14"/><rect x="26" y="8" width="12" height="12"/>
      <rect x="46" y="18" width="12" height="8"/><rect x="66" y="26" width="12" height="6"/>
      <rect x="86" y="34" width="12" height="4"/><rect x="106" y="40" width="12" height="4"/>
    </g>
    <line x1="0" y1="66" x2="222" y2="66" stroke="#ccc"/>
    <g font-size="4.5" fill="#666" font-family="Montserrat, sans-serif">
      <text x="5" y="74">CN</text><text x="25" y="74">US</text><text x="45" y="74">JP</text><text x="65" y="74">UK</text>
      <text x="85" y="74">DE</text><text x="105" y="74">FR</text><text x="125" y="74">IN</text><text x="145" y="74">BR</text>
      <text x="165" y="74">KR</text><text x="185" y="74">CA</text><text x="205" y="74">AU</text>
    </g>
  </svg>
</section>

<!-- Business Model -->
<section class="slide" style="left:478px;top:662px;width:444px;height:116px">
  <div class="hdr"><span class="dot"></span>Business Model</div>
  <div class="bare" style="left:27px;top:28px;color:var(--icon)"><svg class="ico md"><use href="#i-tag"/></svg></div>
  <div class="bare" style="left:27px;top:49px;color:var(--icon)"><svg class="ico md"><use href="#i-coin"/></svg></div>
  <div class="bare" style="left:27px;top:73px;color:var(--icon)"><svg class="ico md"><use href="#i-card"/></svg></div>
  <div class="bare" style="left:27px;top:93px;color:var(--icon)"><svg class="ico md"><use href="#i-star"/></svg></div>
  <div class="bar-row" style="left:62px;top:31px;width:186px">Transactional pricing</div>
  <div class="bar-row" style="left:62px;top:51px;width:224px">Brindlecart: 10c per task (USD)</div>
  <div class="bar-row" style="left:62px;top:75px;width:280px">Credit and top up like a pre-paid phone card</div>
  <div class="bar-row" style="left:62px;top:95px;width:302px">Bonus credit for higher top up amounts</div>
</section>

<!-- Go To Market -->
<section class="slide" style="left:11px;top:792px;width:442px;height:120px">
  <div class="hdr"><span class="dot"></span>Go To Market</div>
  <div class="abs tiny" style="left:20px;top:22px;width:412px">Brindlecart has recently achieved market fit, with 8 paying SME customers in 4 countries. A pilot project is also in progress with a major WA insurer. Brindlecart is a naturally viral product, with our customers sending an effective demonstration of Brindlecart to their customers. Multiple of our paying users are customers of other customers.</div>
  <div class="abs tiny" style="left:14px;top:54px;width:56px">Our go to market plan now is to establish a repeatable sales process:</div>
  <svg class="abs" style="left:70px;top:46px" width="170" height="70" viewBox="0 0 170 70">
    <ellipse cx="70" cy="34" rx="68" ry="30" fill="#eee" stroke="#ccc"/>
    <ellipse cx="84" cy="38" rx="52" ry="22" fill="#e2e2e2" stroke="#ccc"/>
    <ellipse cx="96" cy="42" rx="36" ry="15" fill="#d6d6d6" stroke="#ccc"/>
    <line x1="120" y1="10" x2="170" y2="10" stroke="#ccc"/>
    <line x1="130" y1="34" x2="170" y2="34" stroke="#ccc"/>
    <line x1="118" y1="54" x2="170" y2="54" stroke="#ccc"/>
  </svg>
  <div class="abs tiny" style="left:246px;top:48px;width:192px">Target medium-large fleets in market segments where there is no existing player, or where the customer cannot be retrained; stakeholders including retail, mining, insurance repairs and healthcare.</div>
  <div class="abs tiny" style="left:246px;top:76px;width:192px">Establish recurrent referral and collaboration from targeting customers similar to those for whom we have demonstrated that Brindlecart solves a problem worth paying for.</div>
  <div class="abs tiny" style="left:246px;top:98px;width:192px">Target specific geographic regions to maximise network effect, starting with Australia, Singapore and London.</div>
</section>

<!-- Our Team -->
<section class="slide" style="left:476px;top:790px;width:448px;height:124px">
  <div class="abs" style="left:0;top:0;width:144px;height:124px;background:var(--grey)"></div>
  <div class="abs" style="left:60px;top:34px;width:22px;height:22px;border-radius:50%;background:#fff"></div>
  <div class="abs" style="left:0;top:70px;width:144px;text-align:center;color:#fff;font-size:11px;letter-spacing:1px">Our Team</div>
  <div class="abs small" style="left:158px;top:26px;width:280px;font-size:8px;line-height:1.15">
    <div style="margin-bottom:6px">✓&nbsp;&nbsp;&nbsp;Unique access to technical talent pipeline from our partnership with and colocation at CTU</div>
    <div style="margin-bottom:6px">✓&nbsp;&nbsp;&nbsp;Battle hardened from bootstrapping for 3 years</div>
    <div style="margin-bottom:6px">✓&nbsp;&nbsp;&nbsp;All key players have skin in the game</div>
    <div>✓&nbsp;&nbsp;&nbsp;Founder &amp; board's commercial experience</div>
  </div>
</section>

<!-- Finance -->
<section class="slide" style="left:6px;top:924px;width:444px;height:116px">
  <div class="hdr"><span class="dot"></span>Finance &amp; Opportunity</div>
  <div class="abs small" style="left:38px;top:40px;font-size:8px">2016</div>
  <div class="abs small" style="left:202px;top:40px;font-size:8px">Now</div>
  <div class="abs small" style="left:340px;top:40px;font-size:8px">6-8 months</div>
  <svg class="abs" style="left:20px;top:54px" width="400" height="14" viewBox="0 0 400 14">
    <line x1="0" y1="6" x2="400" y2="6" stroke="#ccc"/>
    <line x1="42" y1="0" x2="42" y2="12" stroke="#ccc"/>
    <line x1="196" y1="0" x2="196" y2="12" stroke="#ccc"/>
    <line x1="350" y1="0" x2="350" y2="12" stroke="#ccc"/>
  </svg>
  <div class="abs small gold" style="left:30px;top:78px;font-size:7px">$200K "FFF"</div>
  <div class="abs small gold" style="left:196px;top:76px;font-size:7px">Deal details</div>
  <div class="abs small gold" style="left:332px;top:74px;font-size:7px">Planned raise</div>
</section>

<!-- Fuel Growth A -->
<section class="slide" style="left:472px;top:928px;width:442px;height:116px">
  <div class="hdr"><span class="dot"></span>How to Fuel Growth</div>
  <div class="abs" style="left:172px;top:40px;width:104px;height:56px;border-radius:50%;background:var(--circle)"></div>
  <div class="abs" style="left:214px;top:58px;width:20px;height:20px;border-radius:50%;background:#fff"></div>
  <div class="tile" style="left:126px;top:34px;width:64px;height:34px"><svg class="ico lg"><use href="#i-monitor"/></svg></div>
  <div class="tile" style="left:254px;top:30px;width:64px;height:34px"><svg class="ico lg"><use href="#i-eye"/></svg></div>
  <div class="tile" style="left:126px;top:74px;width:64px;height:34px"><svg class="ico lg"><use href="#i-target"/></svg></div>
  <div class="tile" style="left:254px;top:72px;width:64px;height:36px"><svg class="ico lg"><use href="#i-route"/></svg></div>
  <div class="abs small center" style="left:30px;top:44px;width:90px">Digital marketing<br>expertise</div>
  <div class="abs small center" style="left:30px;top:86px;width:90px">Activation of<br>digital campaign</div>
  <div class="abs small" style="left:324px;top:44px">Ramp up UX efforts</div>
  <div class="abs small" style="left:324px;top:84px">Customer journey<br>management</div>
</section>

<!-- Fuel Growth B -->
<section class="slide" style="left:10px;top:1052px;width:442px;height:120px">
  <div class="hdr"><span class="dot"></span>How to Fuel Growth</div>
  <div class="abs" style="left:172px;top:38px;width:104px;height:58px;border-radius:50%;background:var(--circle)"></div>
  <div class="tile orange" style="left:126px;top:30px;width:64px;height:30px"><svg class="ico lg"><use href="#i-monitor"/></svg></div>
  <div class="tile orange" style="left:244px;top:30px;width:64px;height:30px"><svg class="ico lg"><use href="#i-eye"/></svg></div>
  <div class="tile orange" style="left:126px;top:72px;width:64px;height:30px"><svg class="ico lg"><use href="#i-target"/></svg></div>
  <div class="tile orange" style="left:244px;top:72px;width:64px;height:30px"><svg class="ico lg"><use href="#i-route"/></svg></div>
  <div class="abs" style="left:190px;top:46px;width:68px;height:44px;border-radius:50%;background:var(--circle)"></div>
  <div class="abs" style="left:214px;top:58px;width:20px;height:20px;border-radius:50%;background:#fff"></div>
  <div class="abs small center" style="left:28px;top:40px;width:90px">Digital marketing<br>expertise</div>
  <div class="abs small center" style="left:28px;top:82px;width:90px">Activation of<br>digital campaign</div>
  <div class="abs small" style="left:324px;top:42px">Ramp up UX efforts</div>
  <div class="abs small" style="left:324px;top:82px">Customer journey<br>management</div>
</section>

<!-- Summary -->
<section class="slide" style="left:480px;top:1048px;width:442px;height:124px">
  <div class="abs photo-globe" role="img" aria-label="Close-up photo of a desk globe" style="left:0;top:0;width:170px;height:124px"></div>
  <div class="abs" style="left:268px;top:8px;font-size:11px;letter-spacing:1px">Summary</div>
  <div class="abs small" style="left:210px;top:28px;width:226px;font-size:6.8px;line-height:1.2">
    <div style="margin-bottom:6px">➢&nbsp;&nbsp;A clear problem for a big market</div>
    <div style="margin-bottom:6px">➢&nbsp;&nbsp;The right people and a great pipeline of talent</div>
    <div style="margin-bottom:6px">➢&nbsp;&nbsp;Great technology foundation and technical skills</div>
    <div style="margin-bottom:6px">➢&nbsp;&nbsp;Paying customers in multiple countries</div>
    <div>➢&nbsp;&nbsp;A clear opportunity for capital to ramp up and drive the growth engine</div>
  </div>
  <div class="abs" style="left:424px;top:112px;width:8px;height:8px;border-radius:50%;background:var(--blue)"></div>
</section>

</body>
</html>
```